Presentation - power point and pdf format

I have two versions of and existing presentation that I would like to have cleaned up and made to look more stylized, slick and professional.
Updates
Reason: Hello I am traveling and have delays in responding. If you do not hear from me allow me some time for feedback.
thank you, Marisol
Reason: Designers I will not be giving any feedback until Monday as I am traveling. Thank you for your patience.
Target Market(s)
Companies would buy this tour in bulk such as Cruise Lines, Hotels, Tour Operators. It has to be professional but fun and colorful as we are dealing with top executives at these companies who need to see the potential of their consumer buying it while they are on vacation.
Industry/Entity Type
It Professional
Look and feel
Each slider illustrates characteristics of the customer's brand and the style your logo design should communicate.

```html
<!DOCTYPE html>
<html lang="en">
<head>
<meta charset="utf-8">
<title>Experience the Flavours</title>
<link href="https://fonts.googleapis.com/css2?family=Carlito:wght@400;700&display=swap" rel="stylesheet">
<style>
  :root {
    --plank-white: #f4f3f1;
    --plank-white-line: #dcdad6;
    --plank-yellow: #fbc94a;
    --plank-yellow-light: #fdd873;
    --plank-line: #f0a92a;
    --title-box: #fcc300;
    --title-text: #5e8f3c;
    --caption: #8c4a10;
    --paella-a: #6b4a2c;
    --paella-b: #c9892f;
    --mojito-a: #c9dfa0;
    --mojito-b: #6f8a3b;
    --coffee-a: #6e5a48;
    --coffee-b: #d8cbb8;
  }
  html, body {
    margin: 0;
    padding: 0;
    overflow: hidden;
    background: #ffffff;
  }
  .slide {
    position: relative;
    width: 1200px;
    height: 900px;
    overflow: hidden;
    font-family: "Carlito", "Calibri", sans-serif;
    background:
      repeating-linear-gradient(90deg,
        transparent 0 60px,
        var(--plank-line) 60px 62px,
        transparent 62px 64px),
      linear-gradient(90deg,
        var(--plank-yellow) 0%, var(--plank-yellow-light) 30%,
        var(--plank-yellow) 55%, var(--plank-yellow-light) 80%, var(--plank-yellow) 100%);
  }
  .top-band {
    position: absolute;
    left: 0; top: 0;
    width: 1200px;
    height: 181px;
    background:
      repeating-linear-gradient(90deg,
        transparent 0 60px,
        var(--plank-white-line) 60px 62px,
        transparent 62px 64px),
      var(--plank-white);
  }
  .slide-title {
    position: absolute;
    left: 627px; top: 62px;
    width: 535px; height: 67px;
    margin: 0;
    background: var(--title-box);
    color: var(--title-text);
    font-size: 37px;
    font-weight: 700;
    line-height: 67px;
    text-align: center;
    box-shadow: 3px 4px 6px rgba(0,0,0,0.3);
  }
  .dish-photo {
    position: absolute;
    width: 315px;
    height: 210px;
    border-radius: 12px;
  }
  .dish-photo::after {
    content: "";
    position: absolute;
    left: 0; top: 214px;
    width: 315px; height: 50px;
    border-radius: 12px 12px 0 0;
    background: inherit;
    opacity: 0.25;
    -webkit-mask-image: linear-gradient(to bottom, #000, transparent);
    mask-image: linear-gradient(to bottom, #000, transparent);
  }
  .dish-photo--paella {
    left: 160px; top: 220px;
    background: radial-gradient(ellipse at 55% 55%, var(--paella-b), var(--paella-a));
  }
  .dish-photo--mojito {
    left: 720px; top: 430px;
    background: radial-gradient(ellipse at 50% 45%, var(--mojito-a), var(--mojito-b));
  }
  .dish-photo--coffee {
    left: 160px; top: 641px;
    background: linear-gradient(135deg, var(--coffee-a), var(--coffee-b));
  }
  .caption {
    position: absolute;
    margin: 0;
    color: var(--caption);
    font-size: 29px;
    font-weight: 700;
    white-space: nowrap;
    text-shadow: 2px 2px 3px rgba(0,0,0,0.25);
  }
  .caption--paella { left: 512px; top: 308px; }
  .caption--mojito { left: 278px; top: 519px; }
  .caption--coffee { left: 528px; top: 729px; }
</style>
</head>
<body>
<main class="slide">
  <div class="top-band"></div>
  <h1 class="slide-title">experience the FLAVOURS</h1>

  <div class="dish-photo dish-photo--paella" role="img" aria-label="Photo of a seafood paella with mussels, shrimp, squid and a red chili in a black pan"></div>
  <p class="caption caption--paella">a colorful CUBAN PAELLA</p>

  <div class="dish-photo dish-photo--mojito" role="img" aria-label="Photo of a mojito glass with ice, mint leaves and a lime half"></div>
  <p class="caption caption--mojito">enjoy a CUBAN MOJITO</p>

  <div class="dish-photo dish-photo--coffee" role="img" aria-label="Photo of a small glass of Cuban coffee on a saucer beside a glass of liqueur"></div>
  <p class="caption caption--coffee">and a great FINALE with a CAFECITO</p>
</main>
</body>
</html>
```